Property Management Services Proposal - Powerpoint template

We need a proposal template for our multifamily property management services. We have a simple/generic handout that we use (uploaded here) but we need something for an actual proposal/client presentation standpoint. A powerpoint file that includes company/team overview, some placeholders for the specific client we would be proposing too, etc. Website is www.kellovanpropertygroup.com

Target Market(s)

Residential/Multifamily Property Owners and Investors

Industry/Entity Type

Real Estate

Font styles to use
Sans Serif

Colors
0355a3
f78f20
9d9d9d
ffffff

Requirements
Must have
• Logo, color scheme (orange, navy, gray) - clean look but not overly simple. Placeholders for specific projects, case studies, timelines, photos, graphs, etc.

```html
<!DOCTYPE html>
<html lang="en">
<head>
<meta charset="utf-8">
<title>Kellovan Property Group – Proposal Template Overview</title>
<link href="https://fonts.googleapis.com/css2?family=Raleway:wght@300;400;600;700;800&display=swap" rel="stylesheet">
<style>
:root{
  --navy:#0355a3;
  --navy-deep:#1d4f80;
  --orange:#f78f20;
  --gray:#9d9d9d;
  --white:#ffffff;
  --ink:#555a60;
  --soft:#eef0f2;
  --rule:#dcdfe3;
}
*{box-sizing:border-box;margin:0;padding:0}
html,body{width:1200px;height:3331px;overflow:hidden;background:#e6e7e9}
body{font-family:"Raleway",Arial,sans-serif;color:var(--ink)}
.deck{display:grid;grid-template-columns:repeat(3,1fr);grid-auto-rows:218.3px;gap:4px;width:1200px;height:3331px}
.last-row{grid-column:1/-1;display:flex;justify-content:center;gap:4px}
.last-row .slide{width:397.3px}
.slide{position:relative;overflow:hidden;background:var(--white)}
.abs{position:absolute}
.st{position:absolute;left:10px;right:10px;top:8px;font-size:12px;font-weight:400;letter-spacing:.5px;color:#555;border-bottom:1px solid var(--rule);padding-bottom:4px;text-transform:uppercase}
.st.light{color:#fff;border-color:rgba(255,255,255,.35)}
.ft{position:absolute;left:8px;right:8px;bottom:4px;display:flex;align-items:center;gap:5px;font-size:4.5px;color:var(--gray)}
.ft b{font-size:8px;font-weight:800;color:var(--orange)}
.ft i{margin-left:auto;font-style:normal}
.p{font-size:4.8px;line-height:1.45;color:#8a8f95}
.p.w{color:rgba(255,255,255,.85)}
.h{font-size:6.5px;font-weight:700;color:#444}
.h.w{color:#fff}
.ph{position:absolute}
.brick{background:linear-gradient(165deg,#aebfcd 0%,#b0664b 38%,#7a4130 75%,#5a5c48 100%)}
.siding{background:linear-gradient(170deg,#c7d2dc 0%,#7e807c 45%,#5b5d58 100%)}
.green{background:linear-gradient(180deg,#b6c9dd 0%,#9aae9a 55%,#5f7d44 100%)}
.city{background:linear-gradient(180deg,#9fb0c1 0%,#6d7f91 60%,#4d5b69 100%)}
.navy{background:var(--navy)}
.orange{background:var(--orange)}
.grayb{background:var(--gray)}
.dot{display:inline-flex;align-items:center;justify-content:center;border-radius:50%;color:#fff;font-weight:700}
.logo{text-align:center;line-height:1}
.logo .mk{font-weight:800;color:var(--orange);letter-spacing:1px}
.logo .nm{display:block;font-weight:600;color:var(--navy);letter-spacing:.6px;text-transform:uppercase}
.corner{position:absolute;right:0;bottom:0;width:120px;height:70px;background:#fff;clip-path:polygon(100% 0,100% 100%,0 100%)}
.corner .logo{position:absolute;right:8px;bottom:8px}
.btn{display:inline-block;background:var(--orange);color:#fff;font-size:5px;padding:3px 8px}
table{border-collapse:collapse}
</style>
</head>
<body>
<main class="deck">

<!-- Row 1 -->
<section class="slide cover-logo">
  <div class="logo abs" style="left:120px;top:52px">
    <span class="mk" style="font-size:34px">KPG</span>
    <span class="nm" style="font-size:6px;margin-top:4px">Kellovan Property Group</span>
    <span class="nm" style="font-size:4.5px;margin-top:3px;color:var(--gray)">Proposal Content</span>
  </div>
</section>

<section class="slide cover-photo">
  <div class="ph city" role="img" aria-label="Office interior photo, darkened" style="inset:0;background:linear-gradient(180deg,#6f7780,#4b535c)"></div>
  <div class="abs" style="left:10px;top:42px;color:#fff">
    <div style="font-size:20px;font-weight:700">Your Title Here</div>
    <div style="font-size:6px;text-align:right">Your Subtitle Goes Here</div>
  </div>
  <div class="logo abs" style="left:240px;top:38px"><span class="mk" style="font-size:30px">KPG</span></div>
</section>

<section class="slide cover-navy">
  <div class="ph" role="img" aria-label="Office interior photo with navy tint" style="inset:0;background:linear-gradient(135deg,#1f5d99,#0f3f70)"></div>
  <div class="abs" style="left:0;right:0;top:50px;text-align:center;color:#fff">
    <div style="font-size:16px;font-weight:700">YOUR TITLE GOES HERE</div>
    <div style="font-size:5.5px;margin-top:2px;text-align:right;padding-right:100px">Your Subtitle Goes Here</div>
  </div>
  <div class="corner"><div class="logo"><span class="mk" style="font-size:16px">KPG</span><span class="nm" style="font-size:3.5px">Kellovan Property Group</span></div></div>
</section>

<!-- Row 2 -->
<section class="slide agenda">
  <h2 class="st">Our Agenda</h2>
  <div class="abs" style="left:12px;top:36px;width:180px">
    <div style="display:flex;gap:5px;margin-bottom:12px"><span class="dot navy" style="width:14px;height:10px;border-radius:0;font-size:5px">01</span><div><div class="h">Agenda One</div><div class="p">Lorem ipsum dolor sit amet, consectetur.</div></div></div>
    <div style="display:flex;gap:5px;margin-bottom:12px"><span class="dot navy" style="width:14px;height:10px;border-radius:0;font-size:5px">02</span><div><div class="h">Agenda Two</div><div class="p">Lorem ipsum dolor sit amet, consectetur.</div></div></div>
    <div style="display:flex;gap:5px"><span class="dot navy" style="width:14px;height:10px;border-radius:0;font-size:5px">03</span><div><div class="h">Agenda Three</div><div class="p">Lorem ipsum dolor sit amet, consectetur.</div></div></div>
  </div>
  <div class="abs" style="left:200px;top:36px;width:180px">
    <div style="display:flex;gap:5px;margin-bottom:12px"><span class="dot navy" style="width:14px;height:10px;border-radius:0;font-size:5px">04</span><div><div class="h">Agenda Four</div><div class="p">Lorem ipsum dolor sit amet, consectetur.</div></div></div>
    <div style="display:flex;gap:5px;margin-bottom:12px"><span class="dot navy" style="width:14px;height:10px;border-radius:0;font-size:5px">05</span><div><div class="h">Agenda Five</div><div class="p">Lorem ipsum dolor sit amet, consectetur.</div></div></div>
    <div style="display:flex;gap:5px"><span class="dot navy" style="width:14px;height:10px;border-radius:0;font-size:5px">06</span><div><div class="h">Agenda Six</div><div class="p">Lorem ipsum dolor sit amet, consectetur.</div></div></div>
  </div>
  <div class="ft"><b>KPG</b><span>www.kellovanpropertygroup.com</span><i>4</i></div>
</section>

<section class="slide photo-collage">
  <div class="abs orange" style="left:0;top:0;width:48%;height:35%;padding:8px"><div class="p w">Lorem ipsum dolor sit amet, consectetur adipiscing elit, sed do eiusmod tempor incididunt ut labore.</div></div>
  <div class="ph brick" role="img" aria-label="Brick apartment building" style="left:48%;top:0;width:52%;height:52%"></div>
  <div class="ph brick" role="img" aria-label="Apartment building with trees" style="left:0;top:35%;width:48%;height:65%"></div>
  <div class="abs" style="left:50%;top:56%;width:22%"><div class="p">Lorem ipsum dolor sit amet, consectetur adipiscing elit sed do eiusmod tempor.</div></div>
  <div class="ph brick" role="img" aria-label="Building entrance" style="left:74%;top:55%;width:26%;height:45%"></div>
</section>

<section class="slide four-cards">
  <h2 class="st">Your Title Here</h2>
  <div class="abs" style="left:10px;right:10px;top:40px;height:140px;display:grid;grid-template-columns:repeat(4,1fr)">
    <div class="navy" style="padding:10px 6px;text-align:center"><span class="dot" style="width:14px;height:14px;border:1px solid #fff"></span><div class="h w" style="margin:6px 0 4px">Heading Here</div><div class="p w">Lorem ipsum dolor sit amet consectetur adipiscing elit.</div></div>
    <div style="background:#6d7f93;padding:10px 6px;text-align:center"><span class="dot" style="width:14px;height:14px;border:1px solid #fff"></span><div class="h w" style="margin:6px 0 4px">Heading Here</div><div class="p w">Lorem ipsum dolor sit amet consectetur adipiscing elit.</div></div>
    <div class="orange" style="padding:10px 6px;text-align:center"><span class="dot" style="width:14px;height:14px;border:1px solid #fff"></span><div class="h w" style="margin:6px 0 4px">Heading Here</div><div class="p w">Lorem ipsum dolor sit amet consectetur adipiscing elit.</div></div>
    <div style="background:var(--navy-deep);padding:10px 6px;text-align:center"><span class="dot" style="width:14px;height:14px;border:1px solid #fff"></span><div class="h w" style="margin:6px 0 4px">Heading Here</div><div class="p w">Lorem ipsum dolor sit amet consectetur adipiscing elit.</div></div>
  </div>
  <div class="ft"><b>KPG</b><span>www.kellovanpropertygroup.com</span><i>6</i></div>
</section>

<!-- Row 3 -->
<section class="slide divider-white">
  <div class="abs" style="right:30px;top:40px;text-align:right">
    <div class="logo" style="display:inline-block"><span class="mk" style="font-size:20px">KPG</span><span class="nm" style="font-size:3.5px">Kellovan Property Group</span></div>
    <div style="font-size:14px;font-weight:800;color:#444;margin-top:8px">DIVIDER PAGE</div>
    <div class="p">Your Subtitle Here</div>
  </div>
  <div class="ft"><b>KPG</b><span>www.kellovanpropertygroup.com</span><i>7</i></div>
</section>

<section class="slide text-bullets">
  <h2 class="st">Text &amp; Bullet Area</h2>
  <div class="abs" style="left:12px;top:36px;width:110px">
    <div class="h" style="color:var(--navy)">Heading Goes Here</div>
    <div class="p" style="margin-top:5px">Lorem ipsum dolor sit amet, consectetur adipiscing elit, sed do eiusmod tempor incididunt ut labore et dolore magna aliqua. Ut enim ad minim veniam.</div>
    <div class="p" style="margin-top:5px">Quis nostrud exercitation ullamco laboris nisi ut aliquip ex ea commodo.</div>
  </div>
  <div class="abs" style="left:135px;top:36px;display:grid;grid-template-columns:1fr 1fr;column-gap:14px;row-gap:7px;width:245px">
    <div style="display:flex;gap:4px;align-items:center"><span class="dot navy" style="width:9px;height:9px"></span><span class="h" style="font-weight:400">Your Text Here</span></div>
    <div style="display:flex;gap:4px;align-items:center"><span class="dot navy" style="width:9px;height:9px"></span><span class="h" style="font-weight:400">Your Text Here</span></div>
    <div style="display:flex;gap:4px;align-items:center"><span class="dot grayb" style="width:9px;height:9px"></span><span class="h" style="font-weight:400">Your Text Here</span></div>
    <div style="display:flex;gap:4px;align-items:center"><span class="dot grayb" style="width:9px;height:9px"></span><span class="h" style="font-weight:400">Your Text Here</span></div>
    <div style="display:flex;gap:4px;align-items:center"><span class="dot orange" style="width:9px;height:9px"></span><span class="h" style="font-weight:400">Your Text Here</span></div>
    <div style="display:flex;gap:4px;align-items:center"><span class="dot orange" style="width:9px;height:9px"></span><span class="h" style="font-weight:400">Your Text Here</span></div>
    <div style="display:flex;gap:4px;align-items:center"><span class="dot navy" style="width:9px;height:9px"></span><span class="h" style="font-weight:400">Your Text Here</span></div>
    <div style="display:flex;gap:4px;align-items:center"><span class="dot navy" style="width:9px;height:9px"></span><span class="h" style="font-weight:400">Your Text Here</span></div>
    <div style="display:flex;gap:4px;align-items:center"><span class="dot grayb" style="width:9px;height:9px"></span><span class="h" style="font-weight:400">Your Text Here</span></div>
    <div style="display:flex;gap:4px;align-items:center"><span class="dot grayb" style="width:9px;height:9px"></span><span class="h" style="font-weight:400">Your Text Here</span></div>
  </div>
  <div class="ft"><b>KPG</b><span>www.kellovanpropertygroup.com</span><i>8</i></div>
</section>

<section class="slide icon-columns" style="display:grid;grid-template-columns:repeat(5,1fr)">
  <div style="background:#1d5b92;padding:40px 6px 0;text-align:center"><span class="dot" style="width:16px;height:16px;border:1px solid #fff"></span><div class="h w" style="font-size:8px;margin:28px 0 5px">Heading Here</div><div class="p w">Lorem ipsum dolor sit amet consectetur elit.</div></div>
  <div style="background:#2c6ba3;padding:40px 6px 0;text-align:center"><span class="dot" style="width:16px;height:16px;border:1px solid #fff"></span><div class="h w" style="font-size:8px;margin:28px 0 5px">Heading Here</div><div class="p w">Lorem ipsum dolor sit amet consectetur elit.</div></div>
  <div style="background:#3c7ab2;padding:40px 6px 0;text-align:center"><span class="dot" style="width:16px;height:16px;border:1px solid #fff"></span><div class="h w" style="font-size:8px;margin:28px 0 5px">Heading Here</div><div class="p w">Lorem ipsum dolor sit amet consectetur elit.</div></div>
  <div style="background:#2c6ba3;padding:40px 6px 0;text-align:center"><span class="dot" style="width:16px;height:16px;border:1px solid #fff"></span><div class="h w" style="font-size:8px;margin:28px 0 5px">Heading Here</div><div class="p w">Lorem ipsum dolor sit amet consectetur elit.</div></div>
  <div style="background:#1d5b92;padding:40px 6px 0;text-align:center"><span class="dot" style="width:16px;height:16px;border:1px solid #fff"></span><div class="h w" style="font-size:8px;margin:28px 0 5px">Heading Here</div><div class="p w">Lorem ipsum dolor sit amet consectetur elit.</div></div>
</section>

<!-- Row 4 -->
<section class="slide mockup-area">
  <h2 class="st">Our Mockup Area</h2>
  <div class="abs" style="left:0;right:0;top:110px;height:80px;background:#e9eaec"></div>
  <div class="ph" role="img" aria-label="Laptop mockup showing company logo" style="left:120px;top:40px;width:170px;height:110px;background:linear-gradient(180deg,#f7f7f7,#d4d6d9);border:6px solid #3b3f44;border-radius:4px"></div>
  <div class="abs" style="left:10px;top:48px;display:grid;gap:14px">
    <span class="navy" style="color:#fff;font-size:5px;padding:3px 10px">Your Text</span>
    <span class="navy" style="color:#fff;font-size:5px;padding:3px 10px">Your Text</span>
    <span class="navy" style="color:#fff;font-size:5px;padding:3px 10px">Your Text</span>
  </div>
  <svg class="abs" style="left:60px;top:50px" width="60" height="70"><path d="M0 3H60M0 30H60M0 56H60" stroke="#9d9d9d" stroke-width=".6"/></svg>
  <div class="ft"><b>KPG</b><span>www.kellovanpropertygroup.com</span><i>10</i></div>
</section>

<section class="slide right-picture">
  <div class="ph" role="img" aria-label="Office photo, grayscale" style="left:0;top:0;width:40%;height:100%;background:linear-gradient(180deg,#8a8f96,#5a5f66)"></div>
  <div class="abs" style="left:25px;top:30px;width:100px;height:100px;border:1.5px solid #fff;border-radius:50%;display:flex;align-items:center;justify-content:center;text-align:center;color:#fff;font-size:9px;font-weight:700;line-height:1.2">RIGHT<br>PICTURE<br>SLIDE</div>
  <div class="abs p w" style="left:20px;top:150px;width:110px">Lorem ipsum dolor sit amet, consectetur adipiscing elit sed do.</div>
  <svg class="abs" style="left:185px;top:40px" width="180" height="110">
    <g fill="var(--navy)"><rect x="0" y="40" width="9" height="70"/><rect x="40" y="20" width="9" height="90"/><rect x="80" y="50" width="9" height="60"/><rect x="120" y="10" width="9" height="100"/></g>
    <g fill="var(--orange)"><rect x="12" y="60" width="9" height="50"/><rect x="52" y="45" width="9" height="65"/><rect x="92" y="30" width="9" height="80"/><rect x="132" y="55" width="9" height="55"/></g>
  </svg>
  <div class="abs" style="left:178px;top:160px;font-size:18px;font-weight:700;color:#444"><span style="color:var(--orange);font-size:10px">▲</span>85%</div>
  <div class="abs p" style="left:255px;top:162px;width:120px">Lorem ipsum dolor sit amet consectetur adipiscing elit.</div>
</section>

<section class="slide our-mockup">
  <div class="abs navy" style="left:0;right:0;top:0;height:48%"></div>
  <h2 class="st light" style="border:none">Our Mockup</h2>
  <div class="abs" style="left:10px;top:28px;width:190px"><div class="h w" style="font-size:8px">Heading Here</div><div class="p w" style="margin-top:3px">Lorem ipsum dolor sit amet, consectetur adipiscing elit, sed do eiusmod tempor incididunt ut labore.</div></div>
  <div class="ph" role="img" aria-label="Desktop monitor mockup showing company logo" style="left:225px;top:30px;width:160px;height:110px;background:linear-gradient(180deg,#fafafa,#dcdfe2);border:5px solid #2f3338;border-radius:3px"></div>
  <div class="abs" style="left:10px;top:118px;width:200px;display:grid;gap:9px">
    <div style="display:flex;gap:5px"><span class="dot navy" style="width:9px;height:9px;font-size:5px">✓</span><span class="p">Lorem ipsum dolor sit amet, consectetur adipiscing elit sed do.</span></div>
    <div style="display:flex;gap:5px"><span class="dot navy" style="width:9px;height:9px;font-size:5px">✓</span><span class="p">Lorem ipsum dolor sit amet, consectetur adipiscing elit sed do.</span></div>
    <div style="display:flex;gap:5px"><span class="dot navy" style="width:9px;height:9px;font-size:5px">✓</span><span class="p">Lorem ipsum dolor sit amet, consectetur adipiscing elit sed do.</span></div>
  </div>
  <div class="ft"><b>KPG</b><span>www.kellovanpropertygroup.com</span><i>12</i></div>
</section>

<!-- Row 5 -->
<section class="slide line-chart">
  <div class="abs" style="left:14px;top:40px;width:110px">
    <div style="font-size:11px;font-weight:700;color:var(--navy);line-height:1.2">THIS IS LINE<br>CHART SLIDE</div>
    <span class="btn" style="margin:6px 0">YOUR TEXT HERE</span>
    <div class="p">Lorem ipsum dolor sit amet, consectetur adipiscing elit, sed do eiusmod tempor incididunt ut labore.</div>
  </div>
  <svg class="abs" style="left:150px;top:30px" width="230" height="140">
    <g stroke="#e3e5e8" stroke-width=".6"><path d="M0 20H230M0 50H230M0 80H230M0 110H230"/></g>
    <polyline points="0,40 60,95 120,70 180,85 230,10" fill="none" stroke="var(--navy)" stroke-width="2"/>
    <polyline points="0,60 60,55 120,105 180,60 230,75" fill="none" stroke="#3d4652" stroke-width="1.2"/>
    <g fill="#999" font-size="5"><text x="10" y="130">Category 1</text><text x="70" y="130">Category 2</text><text x="130" y="130">Category 3</text><text x="190" y="130">Category 4</text></g>
  </svg>
  <div class="ft"><b>KPG</b><span>www.kellovanpropertygroup.com</span><i>13</i></div>
</section>

<section class="slide title-grid">
  <h2 class="st">Your Title Goes Here</h2>
  <div class="abs" style="left:10px;right:10px;top:36px;height:160px;display:grid;grid-template-columns:1fr 1.3fr 1fr;grid-template-rows:1fr 1fr;gap:3px">
    <div class="ph brick" role="img" aria-label="Apartment complex exterior" style="position:relative"></div>
    <div style="background:#2a6aa3;padding:8px"><div class="h w" style="font-size:8px">Heading Goes Here</div><div class="p w" style="margin-top:3px">Lorem ipsum dolor sit amet consectetur elit.</div></div>
    <div class="ph green" role="img" aria-label="Building with lawn" style="position:relative"></div>
    <div class="navy" style="padding:8px"><div class="h w" style="font-size:8px">Heading Goes Here</div><div class="p w" style="margin-top:3px">Lorem ipsum dolor sit amet consectetur elit.</div></div>
    <div class="ph city" role="img" aria-label="City skyline with fountain" style="position:relative"></div>
    <div class="orange" style="padding:8px"><div class="h w" style="font-size:8px">Heading Goes Here</div><div class="p w" style="margin-top:3px">Lorem ipsum dolor sit amet consectetur elit.</div></div>
  </div>
  <div class="ft"><b>KPG</b><span>www.kellovanpropertygroup.com</span><i>14</i></div>
</section>

<section class="slide about-us">
  <div class="ph green" role="img" aria-label="City park with fountain and skyline" style="inset:0"></div>
  <div class="abs navy" style="right:0;top:55px;width:190px;height:110px;padding:14px 12px">
    <div style="color:#fff;font-size:13px;font-weight:400;letter-spacing:1px">ABOUT US</div>
    <div class="p w" style="margin-top:6px">Lorem ipsum dolor sit amet, consectetur adipiscing elit, sed do eiusmod tempor incididunt ut labore et dolore.</div>
    <div class="p w" style="margin-top:4px">Ut enim ad minim veniam, quis nostrud exercitation ullamco laboris.</div>
  </div>
</section>

<!-- Row 6 -->
<section class="slide divider-navy">
  <div class="ph" role="img" aria-label="Office interior photo with navy tint" style="inset:0;background:linear-gradient(135deg,#1c5a93,#0d3b69)"></div>
  <div class="abs" style="left:0;right:0;top:85px;text-align:center;color:#fff;font-size:13px;font-weight:800">THIS IS YOUR DIVIDER PAGE<div style="font-size:5px;font-weight:400;margin-top:3px">Your Subtitle Goes Here</div></div>
  <div class="corner"><div class="logo"><span class="mk" style="font-size:16px">KPG</span><span class="nm" style="font-size:3.5px">Kellovan Property Group</span></div></div>
</section>

<section class="slide quote-area">
  <h2 class="st">Quote Area</h2>
  <div class="ph brick" role="img" aria-label="Brick building with balconies" style="left:200px;top:30px;width:187px;height:160px"></div>
  <div class="abs navy" style="left:0;top:38px;width:215px;height:140px;padding:20px 16px;color:#fff">
    <div style="font-size:9px;line-height:1.45">" Coming together is a beginning; keeping together is progress; working together is success. "</div>
    <div style="font-size:7px;margin-top:10px">- Jordan Vale</div>
  </div>
  <div class="ft"><b>KPG</b><span>www.kellovanpropertygroup.com</span><i>17</i></div>
</section>

<section class="slide brand-detailed">
  <h2 class="st">Brand Detailed</h2>
  <div class="ph green" role="img" aria-label="Property entrance sign with lawn" style="left:10px;top:32px;width:205px;height:160px"></div>
  <div class="abs" style="left:220px;top:32px;width:167px;height:160px;display:grid;grid-template-columns:1fr 1fr;gap:3px">
    <div class="navy" style="padding:8px"><div class="h w">Heading</div><div class="p w">Lorem ipsum dolor sit amet elit.</div></div>
    <div style="background:var(--soft);padding:8px"><div class="h">Heading</div><div class="p">Lorem ipsum dolor sit amet elit.</div></div>
    <div class="orange" style="padding:8px"><div class="h w">Heading</div><div class="p w">Lorem ipsum dolor sit amet elit.</div></div>
    <div style="background:var(--navy-deep);padding:8px"><div class="h w">Heading</div><div class="p w">Lorem ipsum dolor sit amet elit.</div></div>
  </div>
  <div class="ft"><b>KPG</b><span>www.kellovanpropertygroup.com</span><i>18</i></div>
</section>

<!-- Row 7 -->
<section class="slide product-philosophy">
  <h2 class="st">Product Philosophy</h2>
  <svg class="abs" style="left:148px;top:48px" width="100" height="100" viewBox="0 0 100 100">
    <g fill="none" stroke-width="18">
      <circle cx="50" cy="50" r="34" stroke="var(--navy)" stroke-dasharray="74 300" transform="rotate(-90 50 50)"/>
      <circle cx="50" cy="50" r="34" stroke="var(--gray)" stroke-dasharray="43 300" stroke-dashoffset="-74" transform="rotate(-90 50 50)"/>
      <circle cx="50" cy="50" r="34" stroke="var(--orange)" stroke-dasharray="53 300" stroke-dashoffset="-117" transform="rotate(-90 50 50)"/>
      <circle cx="50" cy="50" r="34" stroke="#3a3f46" stroke-dasharray="44 300" stroke-dashoffset="-170" transform="rotate(-90 50 50)"/>
    </g>
    <g font-size="6" fill="#fff" font-weight="700"><text x="60" y="28">35%</text><text x="72" y="60">20%</text><text x="45" y="86">25%</text><text x="12" y="55">20%</text></g>
  </svg>
  <div class="abs" style="left:12px;top:48px;width:110px;text-align:right"><div class="h" style="color:var(--navy)">Market</div><div class="p">Lorem ipsum dolor sit amet consectetur elit.</div></div>
  <div class="abs" style="left:12px;top:125px;width:110px;text-align:right"><div class="h">Good Strategy</div><div class="p">Lorem ipsum dolor sit amet consectetur elit.</div></div>
  <div class="abs" style="left:275px;top:48px;width:110px"><div class="h">Self Manage</div><div class="p">Lorem ipsum dolor sit amet consectetur elit.</div></div>
  <div class="abs" style="left:275px;top:125px;width:110px"><div class="h" style="color:var(--orange)">Leadership</div><div class="p">Lorem ipsum dolor sit amet consectetur elit.</div></div>
  <div class="ft"><b>KPG</b><span>www.kellovanpropertygroup.com</span><i>19</i></div>
</section>

<section class="slide bar-chart">
  <div class="ph" role="img" aria-label="Faded city skyline" style="inset:0;background:linear-gradient(180deg,#f3f4f6,#d9dde2)"></div>
  <div class="abs" style="left:0;right:0;top:10px;text-align:center;font-size:5px;color:#777"><span style="color:var(--navy)">■</span> Series 1 &nbsp; <span style="color:var(--gray)">■</span> Series 2</div>
  <svg class="abs" style="left:20px;top:25px" width="360" height="140">
    <g fill="var(--navy)"><rect x="10" y="60" width="22" height="80"/><rect x="100" y="40" width="22" height="100"/><rect x="190" y="90" width="22" height="50"/><rect x="280" y="95" width="22" height="45"/></g>
    <g fill="var(--gray)"><rect x="36" y="50" width="22" height="90"/><rect x="126" y="10" width="22" height="130"/><rect x="216" y="85" width="22" height="55"/><rect x="306" y="105" width="22" height="35"/></g>
    <g font-size="6" fill="#555" text-anchor="middle"><text x="21" y="55">4.00</text><text x="47" y="45">4.50</text><text x="111" y="35">5.00</text><text x="137" y="6">6.50</text><text x="201" y="85">2.50</text><text x="227" y="80">2.80</text><text x="291" y="90">2.20</text><text x="317" y="100">1.80</text></g>
  </svg>
  <div class="abs navy" style="left:0;right:0;bottom:0;height:50px;display:grid;grid-template-columns:repeat(4,1fr);padding:8px 10px;gap:8px">
    <div><div class="h w">Asia</div><div class="p w">Lorem ipsum dolor sit.</div></div>
    <div><div class="h w">Africa</div><div class="p w">Lorem ipsum dolor sit.</div></div>
    <div><div class="h w">Europe</div><div class="p w">Lorem ipsum dolor sit.</div></div>
    <div><div class="h w">Euro</div><div class="p w">Lorem ipsum dolor sit.</div></div>
  </div>
</section>

<section class="slide trending">
  <h2 class="st">Trending in the World</h2>
  <div class="ph" role="img" aria-label="World map in gray" style="left:10px;top:34px;width:240px;height:150px;background:radial-gradient(ellipse at 50% 50%,#d2d4d7 0%,#e6e7e9 70%,#fff 100%)"></div>
  <span class="abs dot navy" style="left:35px;top:95px;width:28px;height:28px;font-size:7px">25%</span>
  <span class="abs dot grayb" style="left:110px;top:60px;width:38px;height:38px;font-size:9px">80%</span>
  <span class="abs dot orange" style="left:185px;top:90px;width:32px;height:32px;font-size:8px">75%</span>
  <div class="abs" style="left:262px;top:50px;width:125px;display:grid;gap:14px">
    <div style="display:flex;gap:5px"><span class="dot navy" style="width:10px;height:10px;border-radius:1px"></span><div><div class="h" style="color:var(--navy)">Europe</div><div class="p">Lorem ipsum dolor sit amet.</div></div></div>
    <div style="display:flex;gap:5px"><span class="dot orange" style="width:10px;height:10px;border-radius:1px"></span><div><div class="h" style="color:var(--orange)">Canada</div><div class="p">Lorem ipsum dolor sit amet.</div></div></div>
    <div style="display:flex;gap:5px"><span class="dot grayb" style="width:10px;height:10px;border-radius:1px"></span><div><div class="h">Asia</div><div class="p">Lorem ipsum dolor sit amet.</div></div></div>
  </div>
  <div class="ft"><b>KPG</b><span>www.kellovanpropertygroup.com</span><i>21</i></div>
</section>

<!-- Row 8 -->
<section class="slide vision-mission">
  <h2 class="st">Our Vision &amp; Mission</h2>
  <div class="abs navy" style="left:0;right:0;top:34px;height:155px;display:grid;grid-template-columns:1fr 1fr;padding:14px 16px;gap:14px">
    <div><div class="h w" style="font-size:7px">● Our Vision</div><div style="color:#fff;font-size:7.5px;font-weight:700;margin:5px 0">Go to the Next Level.<br>Without lasting Impact</div><div class="p w">Lorem ipsum dolor sit amet, consectetur adipiscing elit, sed do eiusmod tempor incididunt ut labore et dolore.</div></div>
    <div><div class="h w" style="font-size:7px">● Our Mission</div><div style="color:#fff;font-size:6.5px;line-height:2.1;margin-top:4px">✓ Your Text Here<br>✓ Your Text Here<br>✓ Your Text Here<br>✓ Your Text Here</div></div>
  </div>
  <div class="ft"><b>KPG</b><span>www.kellovanpropertygroup.com</span><i>22</i></div>
</section>

<section class="slide services">
  <h2 class="st">Our Services</h2>
  <div class="ph" role="img" aria-label="Hand holding a small house model" style="left:10px;top:32px;width:160px;height:100px;background:linear-gradient(160deg,#3a4450,#16202b)"></div>
  <div class="abs" style="left:10px;top:138px;width:160px"><div class="h">Your Title Goes Here</div><div class="p">Lorem ipsum dolor sit amet, consectetur adipiscing elit, sed do eiusmod tempor incididunt.</div></div>
  <div class="abs" style="left:190px;top:38px;width:195px;display:grid;gap:16px">
    <div style="display:flex;gap:6px"><span class="dot navy" style="width:14px;height:14px;font-size:6px">1</span><div><div class="h" style="color:var(--navy)">Service Number One</div><div class="p">Lorem ipsum dolor sit amet, consectetur adipiscing.</div></div></div>
    <div style="display:flex;gap:6px"><span class="dot grayb" style="width:14px;height:14px;font-size:6px">2</span><div><div class="h">Service Number Two</div><div class="p">Lorem ipsum dolor sit amet, consectetur adipiscing.</div></div></div>
    <div style="display:flex;gap:6px"><span class="dot orange" style="width:14px;height:14px;font-size:6px">3</span><div><div class="h" style="color:var(--orange)">Service Number Three</div><div class="p">Lorem ipsum dolor sit amet, consectetur adipiscing.</div></div></div>
  </div>
  <div class="ft"><b>KPG</b><span>www.kellovanpropertygroup.com</span><i>23</i></div>
</section>

<section class="slide three-column">
  <h2 class="st">Three Column Description</h2>
  <div class="abs" style="left:12px;top:32px;width:240px;font-size:7.5px;color:#666;line-height:1.35">The explorer for your home and where you find every pie spaces that adds up to your plan.</div>
  <div class="abs" style="left:12px;right:12px;top:62px;display:grid;grid-template-columns:repeat(3,1fr);gap:12px">
    <div class="p">Lorem ipsum dolor sit amet, consectetur adipiscing elit, sed do eiusmod tempor incididunt ut labore et dolore magna aliqua. Ut enim ad minim veniam, quis nostrud exercitation.<br><br>Duis aute irure dolor in reprehenderit in voluptate velit esse cillum dolore.</div>
    <div class="p">Lorem ipsum dolor sit amet, consectetur adipiscing elit, sed do eiusmod tempor incididunt ut labore et dolore magna aliqua. Ut enim ad minim veniam, quis nostrud exercitation.<br><br>Duis aute irure dolor in reprehenderit in voluptate velit esse cillum dolore.</div>
    <div class="p">Lorem ipsum dolor sit amet, consectetur adipiscing elit, sed do eiusmod tempor incididunt ut labore et dolore magna aliqua. Ut enim ad minim veniam, quis nostrud exercitation.<br><br>Duis aute irure dolor in reprehenderit in voluptate velit esse cillum dolore.</div>
  </div>
  <div class="ft"><b>KPG</b><span>www.kellovanpropertygroup.com</span><i>24</i></div>
</section>

<!-- Row 9 -->
<section class="slide team-single">
  <h2 class="st">Our Team</h2>
  <div class="ph" role="img" aria-label="Portrait photo of team member" style="left:166px;top:42px;width:66px;height:66px;border-radius:50%;background:linear-gradient(180deg,#c9ced4,#8d949c)"></div>
  <div class="abs" style="left:120px;top:116px;width:158px;text-align:center"><div class="h">Mr. John Doe</div><div class="p">Position / Title</div><div class="p" style="margin-top:3px">Lorem ipsum dolor sit amet, consectetur adipiscing elit sed do eiusmod tempor.</div></div>
  <div class="ft"><b>KPG</b><span>www.kellovanpropertygroup.com</span><i>25</i></div>
</section>

<section class="slide clients" style="display:grid;grid-template-columns:repeat(4,1fr);grid-template-rows:repeat(3,1fr);align-items:center;justify-items:center;padding:10px;font-weight:700;font-size:8px;color:#5f7d44">
  <span>Cedar Court</span><span style="color:var(--navy)">Birch Hollow</span><span style="color:#7b3f2a">Larkfield Estates</span><span style="color:var(--navy)">Orchard Row</span>
  <span style="color:var(--gray)">Elm Crossing</span>
  <div class="navy" style="grid-column:2/4;width:100%;height:100%;display:flex;align-items:center;justify-content:center;color:#fff;font-size:11px;font-weight:400;text-align:center;line-height:1.2">OUR AWESOME<br>CLIENT</div>
  <span style="color:var(--navy)">Orchard Row Homes</span>
  <span style="color:var(--gray)">Hawthorn Place</span><span style="color:#3b7a3a">Willow Ridge</span><span style="color:#b5302a">Fernside</span><span style="color:#3b7a3a">Maple Terrace</span>
</section>

<section class="slide divider-gray">
  <div class="ph city" role="img" aria-label="City skyline photo, grayscale" style="inset:0;background:linear-gradient(180deg,#9aa1a9,#666d75)"></div>
  <div class="abs navy" style="left:0;top:0;width:90px;height:90px;clip-path:polygon(0 0,100% 0,0 100%)"></div>
  <div class="abs" style="left:0;right:0;top:85px;text-align:center;color:#fff;font-size:13px;font-weight:800">THIS IS YOUR DIVIDER PAGE<div style="font-size:5px;font-weight:400;margin-top:3px">Your Subtitle Goes Here</div></div>
  <div class="corner"><div class="logo"><span class="mk" style="font-size:16px">KPG</span><span class="nm" style="font-size:3.5px">Kellovan Property Group</span></div></div>
</section>

<!-- Row 10 -->
<section class="slide pricing">
  <h2 class="st">Monthly Subscription</h2>
  <div class="abs" style="left:0;right:0;top:78px;height:70px;background:#8e9399"></div>
  <div class="abs" style="left:25px;right:25px;top:48px;display:grid;grid-template-columns:repeat(3,1fr);gap:8px;align-items:start">
    <div style="background:#fff;box-shadow:0 0 2px rgba(0,0,0,.2)"><div class="orange" style="color:#fff;text-align:center;font-size:12px;padding:6px 0">$300</div><div class="p" style="text-align:center;line-height:2.5">Storage<br>Bandwidth<br>Support</div></div>
    <div style="background:#fff;box-shadow:0 0 2px rgba(0,0,0,.2);margin-top:-8px"><div class="navy" style="color:#fff;text-align:center;font-size:14px;padding:8px 0">$900</div><div class="p" style="text-align:center;line-height:2.5">Storage<br>Bandwidth<br>Support<br>Domain</div></div>
    <div style="background:#fff;box-shadow:0 0 2px rgba(0,0,0,.2)"><div style="background:#6f747a;color:#fff;text-align:center;font-size:12px;padding:6px 0">$400</div><div class="p" style="text-align:center;line-height:2.5">Storage<br>Bandwidth<br>Support</div></div>
  </div>
  <div class="ft"><b>KPG</b><span>www.kellovanpropertygroup.com</span><i>28</i></div>
</section>

<section class="slide data-table">
  <h2 class="st">Your Title Goes Here</h2>
  <table class="abs" style="left:20px;top:32px;width:357px;font-size:4.8px;color:#666;text-align:center">
    <tr class="navy" style="color:#fff"><th style="padding:3px">&nbsp;</th><th>Item</th><th>Item</th><th>Item</th><th>Item</th></tr>
    <tr style="background:#f1f3f5"><td style="text-align:left;padding:2.6px 4px">Lorem ipsum</td><td>25</td><td>38</td><td>12</td><td>60</td></tr>
    <tr><td style="text-align:left;padding:2.6px 4px">Lorem ipsum</td><td>14</td><td>22</td><td>47</td><td>33</td></tr>
    <tr style="background:#f1f3f5"><td style="text-align:left;padding:2.6px 4px">Lorem ipsum</td><td>31</td><td>19</td><td>28</td><td>54</td></tr>
    <tr><td style="text-align:left;padding:2.6px 4px">Lorem ipsum</td><td>40</td><td>27</td><td>15</td><td>36</td></tr>
    <tr style="background:#f1f3f5"><td style="text-align:left;padding:2.6px 4px">Lorem ipsum</td><td>18</td><td>44</td><td>23</td><td>29</td></tr>
    <tr><td style="text-align:left;padding:2.6px 4px">Lorem ipsum</td><td>26</td><td>35</td><td>41</td><td>17</td></tr>
    <tr style="background:#f1f3f5"><td style="text-align:left;padding:2.6px 4px">Lorem ipsum</td><td>52</td><td>13</td><td>30</td><td>24</td></tr>
    <tr><td style="text-align:left;padding:2.6px 4px">Lorem ipsum</td><td>21</td><td>39</td><td>16</td><td>45</td></tr>
    <tr style="background:#f1f3f5"><td style="text-align:left;padding:2.6px 4px">Lorem ipsum</td><td>34</td><td>20</td><td>48</td><td>11</td></tr>
    <tr><td style="text-align:left;padding:2.6px 4px">Lorem ipsum</td><td>29</td><td>46</td><td>19</td><td>37</td></tr>
  </table>
  <div class="ft"><b>KPG</b><span>www.kellovanpropertygroup.com</span><i>29</i></div>
</section>

<section class="slide team-four">
  <h2 class="st">Our Team</h2>
  <div class="abs" style="left:14px;right:14px;top:36px;display:grid;grid-template-columns:1fr 1fr;row-gap:18px;column-gap:14px">
    <div style="display:flex;gap:6px"><span class="ph" role="img" aria-label="Team member portrait" style="position:relative;flex:none;width:26px;height:26px;border-radius:50%;background:linear-gradient(#c9ced4,#8d949c)"></span><div><div class="h">Michael Doe</div><div class="p" style="color:var(--orange)">CEO</div><div class="p">Lorem ipsum dolor sit amet consectetur adipiscing elit.</div></div></div>
    <div style="display:flex;gap:6px"><span class="ph" role="img" aria-label="Team member portrait" style="position:relative;flex:none;width:26px;height:26px;border-radius:50%;background:linear-gradient(#c9ced4,#8d949c)"></span><div><div class="h">James Doe</div><div class="p" style="color:var(--orange)">CFO</div><div class="p">Lorem ipsum dolor sit amet consectetur adipiscing elit.</div></div></div>
    <div style="display:flex;gap:6px"><span class="ph" role="img" aria-label="Team member portrait" style="position:relative;flex:none;width:26px;height:26px;border-radius:50%;background:linear-gradient(#c9ced4,#8d949c)"></span><div><div class="h">Jane Doe</div><div class="p" style="color:var(--orange)">Manager</div><div class="p">Lorem ipsum dolor sit amet consectetur adipiscing elit.</div></div></div>
    <div style="display:flex;gap:6px"><span class="ph" role="img" aria-label="Team member portrait" style="position:relative;flex:none;width:26px;height:26px;border-radius:50%;background:linear-gradient(#c9ced4,#8d949c)"></span><div><div class="h">John Doe</div><div class="p" style="color:var(--orange)">Director</div><div class="p">Lorem ipsum dolor sit amet consectetur adipiscing elit.</div></div></div>
  </div>
  <div class="ft"><b>KPG</b><span>www.kellovanpropertygroup.com</span><i>30</i></div>
</section>

<!-- Row 11 -->
<section class="slide testimonials">
  <h2 class="st">Customer Testimonials</h2>
  <div class="ph" role="img" aria-label="Customer portrait" style="left:40px;top:34px;width:36px;height:36px;border-radius:50%;background:linear-gradient(#c9ced4,#8d949c)"></div>
  <div class="abs p" style="left:95px;top:40px;width:280px">Lorem ipsum dolor sit amet, consectetur adipiscing elit, sed do eiusmod tempor incididunt ut labore et dolore magna aliqua. Ut enim ad minim veniam, quis nostrud exercitation.</div>
  <div class="abs navy" style="left:0;right:0;top:104px;height:90px;display:grid;grid-template-columns:repeat(4,1fr);padding:14px 14px;gap:10px;text-align:center">
    <div><span class="dot" style="width:18px;height:18px;border:1px solid #fff"></span><div class="p w" style="margin-top:5px">Lorem ipsum dolor sit amet elit.</div></div>
    <div><span class="dot" style="width:18px;height:18px;border:1px solid #fff"></span><div class="p w" style="margin-top:5px">Lorem ipsum dolor sit amet elit.</div></div>
    <div><span class="dot" style="width:18px;height:18px;border:1px solid #fff"></span><div class="p w" style="margin-top:5px">Lorem ipsum dolor sit amet elit.</div></div>
    <div><span class="dot" style="width:18px;height:18px;border:1px solid #fff"></span><div class="p w" style="margin-top:5px">Lorem ipsum dolor sit amet elit.</div></div>
  </div>
  <div class="ft"><b>KPG</b><span>www.kellovanpropertygroup.com</span><i>31</i></div>
</section>

<section class="slide two-pictures">
  <h2 class="st">Two Pictures Slide</h2>
  <div class="ph brick" role="img" aria-label="Brick apartment building with trees" style="left:10px;top:32px;width:185px;height:150px"></div>
  <div class="ph siding" role="img" aria-label="Apartment building with siding" style="left:202px;top:32px;width:185px;height:150px"></div>
  <div class="ft"><b>KPG</b><span>www.kellovanpropertygroup.com</span><i>32</i></div>
</section>

<section class="slide title-image-text">
  <h2 class="st">Title and Image + Text</h2>
  <div class="ph green" role="img" aria-label="Property entrance sign with flower bed" style="left:160px;top:32px;width:227px;height:110px"></div>
  <div class="abs" style="left:12px;top:118px;width:140px;font-size:8.5px;font-weight:700;color:var(--navy);line-height:1.25">Lorem ipsum color amet, consectetur adipiscing elit ut labore et dolore magna aliqua.</div>
  <div class="abs p" style="left:165px;top:150px;width:220px">Lorem ipsum dolor sit amet, consectetur adipiscing elit, sed do eiusmod tempor incididunt ut labore et dolore magna aliqua.</div>
  <div class="ft"><b>KPG</b><span>www.kellovanpropertygroup.com</span><i>33</i></div>
</section>

<!-- Row 12 -->
<section class="slide sales-comparison">
  <h2 class="st">Sales Comparison</h2>
  <svg class="abs" style="left:15px;top:40px" width="150" height="110">
    <text x="60" y="6" font-size="5" fill="#888">2017 Sales</text>
    <g fill="var(--navy)"><rect x="10" y="50" width="12" height="60"/><rect x="35" y="25" width="12" height="85"/><rect x="60" y="60" width="12" height="50"/><rect x="85" y="20" width="12" height="90"/><rect x="110" y="45" width="12" height="65"/></g>
  </svg>
  <svg class="abs" style="left:235px;top:40px" width="150" height="110">
    <text x="60" y="6" font-size="5" fill="#888">2018 Sales</text>
    <g fill="var(--gray)"><rect x="10" y="30" width="12" height="80"/><rect x="35" y="45" width="12" height="65"/><rect x="60" y="20" width="12" height="90"/><rect x="85" y="40" width="12" height="70"/><rect x="110" y="25" width="12" height="85"/></g>
  </svg>
  <span class="abs dot orange" style="left:186px;top:82px;width:26px;height:26px;font-size:9px">⇄</span>
  <div class="abs" style="left:18px;top:158px;display:flex;gap:5px;align-items:center"><span style="font-size:18px;font-weight:700;color:var(--navy)">45%</span><span class="p" style="width:60px">Lorem ipsum dolor sit amet elit.</span></div>
  <div class="abs" style="left:240px;top:158px;display:flex;gap:5px;align-items:center"><span style="font-size:18px;font-weight:700;color:#777">68%</span><span class="p" style="width:60px">Lorem ipsum dolor sit amet elit.</span></div>
  <div class="ft"><b>KPG</b><span>www.kellovanpropertygroup.com</span><i>34</i></div>
</section>

<section class="slide title-boxes">
  <div class="ph" role="img" aria-label="Faded office photo" style="inset:0;background:linear-gradient(180deg,#a9adb2,#d7d9dc)"></div>
  <div class="abs" style="left:0;right:0;top:20px;text-align:center;color:#fff;font-size:12px">YOUR TITLE GOES HERE</div>
  <div class="abs" style="left:0;right:0;top:85px;height:110px;display:grid;grid-template-columns:repeat(3,1fr)">
    <div class="navy" style="padding:14px 12px"><div class="p w">Lorem ipsum dolor sit amet, consectetur adipiscing elit, sed do eiusmod tempor incididunt ut labore et dolore magna.</div></div>
    <div style="background:#7b8189;padding:14px 12px"><div class="p w">Lorem ipsum dolor sit amet, consectetur adipiscing elit, sed do eiusmod tempor incididunt ut labore et dolore magna.</div></div>
    <div class="orange" style="padding:14px 12px"><div class="p w">Lorem ipsum dolor sit amet, consectetur adipiscing elit, sed do eiusmod tempor incididunt ut labore et dolore magna.</div></div>
  </div>
</section>

<section class="slide us-map">
  <h2 class="st">United States Map</h2>
  <div class="abs" style="left:14px;top:60px;width:110px;display:grid;gap:12px;font-size:5px;color:#fff">
    <div style="display:flex"><span class="navy" style="padding:3px 6px;width:70%">Category 1</span><span style="background:#ccc;color:#555;padding:3px 4px">60%</span></div>
    <div style="display:flex"><span class="navy" style="padding:3px 6px;width:60%">Category 2</span><span style="background:#ccc;color:#555;padding:3px 4px">50%</span></div>
    <div style="display:flex"><span class="navy" style="padding:3px 6px;width:80%">Category 3</span><span style="background:#ccc;color:#555;padding:3px 4px">75%</span></div>
  </div>
  <div class="ph" role="img" aria-label="United States map with highlighted states" style="left:175px;top:45px;width:210px;height:120px;background:linear-gradient(135deg,#9aa0a7,#3f6f9e 50%,#9aa0a7);border-radius:8px"></div>
  <div class="ft"><b>KPG</b><span>www.kellovanpropertygroup.com</span><i>36</i></div>
</section>

<!-- Row 13 -->
<section class="slide title-list-a">
  <h2 class="st">Your Title</h2>
  <div class="ph brick" role="img" aria-label="Apartment complex with parking" style="left:160px;top:28px;width:227px;height:70px"></div>
  <div class="abs" style="left:12px;top:30px;width:140px"><div class="h" style="color:var(--orange)">Good point</div><div class="p">Lorem ipsum dolor sit amet, consectetur adipiscing.</div></div>
  <div class="abs navy" style="left:0;top:100px;width:180px;height:95px;padding:12px"><div class="p w">Lorem ipsum dolor sit amet, consectetur adipiscing elit, sed do eiusmod tempor incididunt ut labore et dolore magna aliqua.</div><div class="p w" style="margin-top:4px">Ut enim ad minim veniam, quis nostrud exercitation.</div></div>
  <div class="abs" style="left:200px;top:112px;width:180px;display:flex;gap:5px"><span class="dot navy" style="width:10px;height:10px"></span><div><div class="h">Build point</div><div class="p">Lorem ipsum dolor sit amet, consectetur adipiscing.</div></div></div>
  <div class="ft"><b>KPG</b><span>www.kellovanpropertygroup.com</span><i>37</i></div>
</section>

<section class="slide title-list-b">
  <h2 class="st">Your Title</h2>
  <div class="abs" style="left:12px;top:34px;width:150px;display:grid;gap:12px">
    <div style="display:flex;gap:5px"><span class="dot navy" style="width:10px;height:10px"></span><div><div class="h" style="color:var(--navy)">Good point</div><div class="p">Lorem ipsum dolor sit amet elit.</div></div></div>
    <div style="display:flex;gap:5px"><span class="dot grayb" style="width:10px;height:10px"></span><div><div class="h">Good</div><div class="p">Lorem ipsum dolor sit amet elit.</div></div></div>
    <div style="display:flex;gap:5px"><span class="dot orange" style="width:10px;height:10px"></span><div><div class="h" style="color:var(--orange)">Sales</div><div class="p">Lorem ipsum dolor sit amet elit.</div></div></div>
  </div>
  <div class="ph" role="img" aria-label="Property sign on a post" style="left:230px;top:28px;width:157px;height:80px;background:linear-gradient(160deg,#d8dfe6,#a67a58 60%,#6f7d5a)"></div>
  <div class="abs navy" style="left:190px;top:105px;width:207px;height:90px;padding:12px"><div class="p w">Lorem ipsum dolor sit amet, consectetur adipiscing elit, sed do eiusmod tempor incididunt ut labore et dolore magna aliqua.</div><div class="p w" style="margin-top:4px">Ut enim ad minim veniam, quis nostrud exercitation.</div></div>
  <div class="ft"><b>KPG</b><span>www.kellovanpropertygroup.com</span><i>38</i></div>
</section>

<section class="slide who-we-are">
  <h2 class="st">Who We Are?</h2>
  <div class="abs" style="left:14px;right:14px;top:38px;display:grid;gap:12px">
    <div style="display:grid;grid-template-columns:80px 1fr;gap:10px"><div style="font-size:8px;color:var(--orange);line-height:1.2">A Title About Contents</div><div class="p">Lorem ipsum dolor sit amet, consectetur adipiscing elit, sed do eiusmod tempor incididunt ut labore et dolore magna aliqua. Ut enim ad minim veniam.</div></div>
    <div style="display:grid;grid-template-columns:80px 1fr;gap:10px"><div style="font-size:8px;color:var(--navy);line-height:1.2">A Title About Contents</div><div class="p">Lorem ipsum dolor sit amet, consectetur adipiscing elit, sed do eiusmod tempor incididunt ut labore et dolore magna aliqua. Ut enim ad minim veniam.</div></div>
    <div style="display:grid;grid-template-columns:80px 1fr;gap:10px"><div style="font-size:8px;color:var(--orange);line-height:1.2">A Title About Contents</div><div class="p">Lorem ipsum dolor sit amet, consectetur adipiscing elit, sed do eiusmod tempor incididunt ut labore et dolore magna aliqua. Ut enim ad minim veniam.</div></div>
  </div>
  <div class="ft"><b>KPG</b><span>www.kellovanpropertygroup.com</span><i>39</i></div>
</section>

<!-- Row 14 -->
<section class="slide three-steps">
  <h2 class="st">Three Steps</h2>
  <div class="abs" style="left:14px;top:40px;width:170px;display:grid;gap:16px">
    <div style="display:flex;gap:6px"><span class="dot navy" style="width:12px;height:12px;font-size:6px">1</span><div><div class="h" style="color:var(--navy)">Sample Text</div><div class="p">Lorem ipsum dolor sit amet, consectetur.</div></div></div>
    <div style="display:flex;gap:6px"><span class="dot grayb" style="width:12px;height:12px;font-size:6px">2</span><div><div class="h">Sample Text</div><div class="p">Lorem ipsum dolor sit amet, consectetur.</div></div></div>
    <div style="display:flex;gap:6px"><span class="dot orange" style="width:12px;height:12px;font-size:6px">3</span><div><div class="h" style="color:var(--orange)">Sample Text</div><div class="p">Lorem ipsum dolor sit amet, consectetur.</div></div></div>
  </div>
  <svg class="abs" style="left:230px;top:28px" width="150" height="170" viewBox="0 0 150 170">
    <g fill="none" stroke-width="14">
      <circle cx="90" cy="40" r="28" stroke="var(--navy)"/>
      <circle cx="50" cy="85" r="28" stroke="var(--gray)"/>
      <circle cx="90" cy="130" r="28" stroke="var(--orange)"/>
    </g>
    <g fill="#fff"><circle cx="90" cy="40" r="12"/><circle cx="50" cy="85" r="12"/><circle cx="90" cy="130" r="12"/></g>
  </svg>
  <div class="ft"><b>KPG</b><span>www.kellovanpropertygroup.com</span><i>40</i></div>
</section>

<section class="slide timeline">
  <h2 class="st">Project Timeline</h2>
  <svg class="abs" style="left:14px;top:32px" width="370" height="160">
    <g font-size="4.5" fill="#777">
      <text x="0" y="8">Description</text>
      <text x="60" y="8">Jan</text><text x="85" y="8">Feb</text><text x="110" y="8">Mar</text><text x="135" y="8">Apr</text><text x="160" y="8">May</text><text x="185" y="8">Jun</text><text x="210" y="8">Jul</text><text x="235" y="8">Aug</text><text x="260" y="8">Sep</text><text x="285" y="8">Oct</text><text x="310" y="8">Nov</text><text x="335" y="8">Dec</text>
      <text x="0" y="24">Planning</text><text x="0" y="38">Research</text><text x="0" y="52">Design</text><text x="0" y="66">Review</text><text x="0" y="80">Approval</text><text x="0" y="94">Launch</text><text x="0" y="108">Marketing</text><text x="0" y="122">Leasing</text>
    </g>
    <g stroke="#e4e6e9" stroke-width=".5"><path d="M0 12H370M0 27H370M0 41H370M0 55H370M0 69H370M0 83H370M0 97H370M0 111H370M0 125H370"/></g>
    <rect x="60" y="17" width="60" height="8" fill="var(--navy)"/>
    <rect x="95" y="31" width="70" height="8" fill="var(--gray)"/>
    <rect x="130" y="45" width="80" height="8" fill="var(--orange)"/>
    <rect x="180" y="59" width="50" height="8" fill="var(--navy)"/>
    <rect x="210" y="73" width="45" height="8" fill="var(--gray)"/>
    <rect x="240" y="87" width="55" height="8" fill="var(--orange)"/>
    <rect x="270" y="101" width="60" height="8" fill="var(--navy)"/>
    <rect x="300" y="115" width="60" height="8" fill="var(--gray)"/>
    <g font-size="4.5" fill="#777"><rect x="60" y="142" width="6" height="5" fill="var(--navy)"/><text x="69" y="146">Phase 1</text><rect x="140" y="142" width="6" height="5" fill="var(--gray)"/><text x="149" y="146">Phase 2</text><rect x="220" y="142" width="6" height="5" fill="var(--orange)"/><text x="229" y="146">Phase 3</text></g>
  </svg>
  <div class="ft"><b>KPG</b><span>www.kellovanpropertygroup.com</span><i>41</i></div>
</section>

<section class="slide key-points">
  <div class="ph siding" role="img" aria-label="Apartment building with siding and balconies" style="left:0;top:0;width:50%;height:100%"></div>
  <div class="abs navy" style="left:50%;top:0;width:50%;height:100%;padding:30px 18px;color:#fff">
    <div style="font-size:13px;letter-spacing:1px">KEY POINTS</div>
    <div style="font-size:5.5px;line-height:2.6;margin-top:10px">● Lorem ipsum dolor sit amet<br>● Consectetur adipiscing elit<br>● Sed do eiusmod tempor<br>● Incididunt ut labore dolore<br>● Ut enim ad minim veniam<br>● Quis nostrud exercitation</div>
  </div>
</section>

<!-- Row 15 -->
<div class="last-row">
  <section class="slide three-bullets">
    <h2 class="st">Three Bullets Area</h2>
    <div class="ph siding" role="img" aria-label="Apartment complex with entrance sign" style="left:0;top:28px;width:100%;height:100px"></div>
    <div class="abs" style="left:30px;right:30px;top:108px;display:grid;grid-template-columns:repeat(3,1fr);text-align:center;gap:10px">
      <div><span class="dot navy" style="width:38px;height:38px;border:3px solid #fff"></span><div class="p" style="margin-top:4px">Lorem ipsum dolor sit amet consectetur.</div></div>
      <div><span class="dot grayb" style="width:38px;height:38px;border:3px solid #fff"></span><div class="p" style="margin-top:4px">Lorem ipsum dolor sit amet consectetur.</div></div>
      <div><span class="dot orange" style="width:38px;height:38px;border:3px solid #fff"></span><div class="p" style="margin-top:4px">Lorem ipsum dolor sit amet consectetur.</div></div>
    </div>
    <div class="ft"><b>KPG</b><span>www.kellovanpropertygroup.com</span><i>43</i></div>
  </section>

  <section class="slide thank-you">
    <div class="ph" role="img" aria-label="Office photo with navy tint" style="inset:0;background:linear-gradient(135deg,#1c5a93,#0c3864)"></div>
    <div class="abs" style="left:20px;top:40px;color:#fff">
      <div style="font-size:20px;font-weight:800">THANK YOU</div>
      <div style="font-size:9px;letter-spacing:.5px">SEND YOUR FEEDBACK</div>
      <div style="font-size:5.5px;line-height:2.3;margin-top:14px">
        <div><span class="dot" style="width:8px;height:8px;background:#fff;color:var(--navy);font-size:5px">⌂</span>&nbsp; 100 Orchard Lane, Suite 200</div>
        <div><span class="dot" style="width:8px;height:8px;background:#fff;color:var(--navy);font-size:5px">✆</span>&nbsp; +1 555 014 2290</div>
        <div><span class="dot" style="width:8px;height:8px;background:#fff;color:var(--navy);font-size:5px">@</span>&nbsp; info@kellovanpropertygroup.com</div>
        <div><span class="dot" style="width:8px;height:8px;background:#fff;color:var(--navy);font-size:5px">◉</span>&nbsp; www.kellovanpropertygroup.com</div>
      </div>
    </div>
    <div class="corner"><div class="logo"><span class="mk" style="font-size:16px">KPG</span><span class="nm" style="font-size:3.5px">Kellovan Property Group</span></div></div>
  </section>
</div>

</main>
</body>
</html>
```